KVL cards

Design business cards for renamed business. Korvane Lighting Limited is a leading contract designer of electronic lighting products sepcialising in LED lighting. Need a design that is simple but clear please. Cards for two persons requried.

Target Market(s)

Professional and technical

Industry/Entity Type

Business

Font styles to use
Sans Serif
Other font styles liked:
• tahoma

Colors
ffcf3e

```html
<!DOCTYPE html>
<html lang="en">
<head>
<meta charset="utf-8">
<title>Korvane Lighting Limited – Business Card</title>
<link rel="stylesheet" href="https://fonts.googleapis.com/css2?family=Open+Sans:wght@400;600&family=PT+Sans+Narrow:wght@400;700&family=Dancing+Script:wght@500&display=swap">
<style>
  :root {
    --backdrop: #262626;
    --card-yellow: #fbd70e;
    --card-yellow-soft: #fde677;
    --glow: #fffbe8;
    --ink: #111a16;
    --tagline-ink: #4a4a4a;
    --frame: rgba(255, 255, 255, 0.75);
    --head-tone: #3c3f52;
  }
  * { margin: 0; padding: 0; box-sizing: border-box; }
  html, body {
    width: 1200px;
    height: 953px;
    overflow: hidden;
    background: var(--backdrop);
  }
  .canvas {
    position: relative;
    width: 1200px;
    height: 953px;
  }
  .business-card {
    position: absolute;
    left: 100px;
    top: 206px;
    width: 1000px;
    height: 542px;
    background:
      radial-gradient(circle at 74% 50%, var(--glow) 0, var(--card-yellow-soft) 22%, var(--card-yellow) 52%),
      var(--card-yellow);
    color: var(--ink);
    font-family: "Open Sans", Tahoma, sans-serif;
  }
  .card-frame {
    position: absolute;
    inset: 20px;
    border: 1.5px solid var(--frame);
  }
  .company-name {
    position: absolute;
    left: 56px;
    top: 42px;
    font-size: 58px;
    line-height: 76px;
    font-weight: 600;
    letter-spacing: -1px;
    white-space: nowrap;
  }
  .company-name .suffix {
    font-size: 38px;
    margin-left: 14px;
    letter-spacing: 0;
  }
  .person-name {
    position: absolute;
    left: 60px;
    top: 144px;
    font-size: 40px;
    font-weight: 600;
  }
  .person-role {
    position: absolute;
    left: 60px;
    top: 204px;
    font-size: 26px;
  }
  .contact {
    position: absolute;
    left: 58px;
    top: 268px;
    list-style: none;
  }
  .contact li { white-space: nowrap; }
  .contact .address { font-size: 27px; font-weight: 600; height: 46px; }
  .contact .email {
    font-family: "PT Sans Narrow", "Arial Narrow", sans-serif;
    font-weight: 700; font-size: 27px; height: 46px;
  }
  .contact .phone { font-size: 26px; font-weight: 600; height: 48px; }
  .contact .website {
    font-family: "PT Sans Narrow", "Arial Narrow", sans-serif;
    font-weight: 700; font-size: 27px;
  }
  .head-illustration {
    position: absolute;
    left: 632px;
    top: 130px;
    width: 236px;
    height: 300px;
    border-radius: 46% 46% 18% 18%;
    background: radial-gradient(ellipse at 50% 40%, #6a6c7c 0, var(--head-tone) 60%, rgba(60, 63, 82, 0.15) 100%);
    opacity: 0.85;
  }
  .tagline {
    position: absolute;
    left: 0;
    right: 0;
    top: 450px;
    text-align: center;
    font-family: "Dancing Script", cursive;
    font-size: 34px;
    font-weight: 500;
    color: var(--tagline-ink);
    white-space: nowrap;
  }
</style>
</head>
<body>
  <main class="canvas">
    <section class="business-card">
      <div class="card-frame"></div>
      <div class="head-illustration" role="img" aria-label="Illustration of a human head in profile drawn from scribbled lines, with a glowing light bulb inside"></div>
      <h1 class="company-name">Korvane Lighting<span class="suffix">Limited</span></h1>
      <p class="person-name">Your Name</p>
      <p class="person-role">CEO</p>
      <ul class="contact">
        <li class="address">18 Marlow st</li>
        <li class="email">KVL@korvanelighting.com</li>
        <li class="phone">0400 555 017</li>
        <li class="website">www.KVLlightingltd.com</li>
      </ul>
      <p class="tagline">designer of electronic lighting products sepcialising in LED lighting</p>
    </section>
  </main>
</body>
</html>
```